Ecommerce website Home Page Design that is clean and elegant

Design a Home page for an ecommerce website. This website products and offerings will be very similar to :

breezyharborcharms.com
maplecrestbazaar.com

Target Market(s)

Consumer and small shops who can order online.

Industry/Entity Type

Retail

Number of Pages Required

1 page

Colors

Designer to choose colors to be used in the design.

Requirements
Must have
• Exact competition with similar products:
• breezyharborcharms.com
• http://www.maplecrestbazaar.com/
• Home page with featured image banner
• List of items on sale or category based items list
• atleast three banners for sale or shipping related offers.
Nice to have
• The logo has very light colors and products will have lots of colors as you can see on competition sites. So the design must consider this so that logo also stands out somewhat for branding purpose.
Should not have
• Design should not have black background

```html
<!DOCTYPE html>
<html lang="en">
<head>
<meta charset="utf-8">
<title>Brightloop Shop – Home</title>
<link href="https://fonts.googleapis.com/css2?family=Mulish:wght@400;600;700&family=Roboto+Condensed:wght@700&family=Dancing+Script:wght@700&display=swap" rel="stylesheet">
<style>
:root{
  --teal:#5ea3b1;
  --teal-dark:#4f929f;
  --orange:#efad3c;
  --red:#d0141b;
  --ink:#333;
  --muted:#666;
  --label-bg:#eeeeee;
  --band:#f2f2f2;
  --footer-dark:#3c3c3c;
  --blue:#0e4a9a;
  --green:#7ac143;
}
*{box-sizing:border-box;margin:0;padding:0}
html,body{width:695px;height:1200px;overflow:hidden}
body{position:relative;background:#f8f8f8;font-family:"Mulish",sans-serif;color:var(--ink)}
.abs{position:absolute}
.topbar{left:0;top:0;width:695px;height:14px;background:#fff;font-size:6.5px;line-height:14px}
.topbar .promo{left:93px}
.topbar .ship{left:333px}
.topbar .chat{left:464px;top:1px;height:12px;width:42px;background:#ddd;text-align:center;line-height:12px;font-size:5px;color:#777}
.topbar .acct{left:518px;text-decoration:underline;color:#557;font-size:5px}
.topbar .cart{left:576px;font-size:5px;text-decoration:underline}
.topbar .count{left:592px;top:3px;width:9px;height:8px;border-radius:4px;background:#aaa;color:#fff;font-size:5px;line-height:8px;text-align:center}
.brand{left:93px;top:27px;font-size:26px;font-weight:700;color:var(--teal);letter-spacing:.5px}
.search{left:232px;top:30px;width:224px;height:23px;background:#fff;border:1px solid #e2e2e2;font-size:7px;color:#777;line-height:21px;padding-left:4px}
.search-btn{left:456px;top:30px;width:30px;height:23px;background:var(--orange)}
.phone{left:496px;top:28px;font-size:15px;color:#333}
.hours{left:500px;top:45px;font-size:7.5px;color:#555}
.nav{left:0;top:70px;width:695px;height:24px;background:var(--teal)}
.nav-inner{left:93px;top:0;width:509px;height:24px;background:var(--teal-dark);display:flex;gap:18px;padding-left:11px;align-items:center;font-size:8.5px;color:#fff}
.photo{display:block}
.hero-main{left:93px;top:98px;width:378px;height:158px;background:linear-gradient(110deg,#8fb85a,#c9c0b6 45%,#e7b7c4 65%,#86ad4e)}
.hero-card{left:4px;top:4px;width:120px;height:150px;background:rgba(255,255,255,.93);text-align:center}
.script{font-family:"Dancing Script",cursive;color:var(--red)}
.hero-card .script{font-size:22px;margin-top:20px}
.hero-card h2{font-weight:400;font-size:16px;color:var(--teal);letter-spacing:1px}
.hero-card p{font-size:8px;color:#555;line-height:12px;margin:5px 10px 0}
.shop-btn{display:inline-block;background:var(--red);color:#fff;font-size:9px;font-weight:700;padding:3px 10px;margin-top:8px;border:1px solid #fff}
.hero-side{left:474px;top:98px;width:128px;height:158px;background:linear-gradient(160deg,#d8e7f3,#e6545c 55%,#3a8fd0)}
.save-card{left:13px;top:6px;width:102px;height:52px;background:rgba(255,255,255,.92);text-align:center}
.save-card .script{font-size:19px;margin-top:4px}
.save-card p{font-size:6.5px;color:var(--teal);line-height:8px}
.hero-side .shop-btn{position:absolute;left:24px;top:133px;font-size:7.5px;margin:0}
.tile-img{background:#fff}
.label{background:var(--label-bg);text-align:center;color:#666;font-size:8px;font-weight:600;letter-spacing:.3px}
.sale{left:93px;top:518px;width:509px;height:82px;background:linear-gradient(90deg,#fff,#e7eef6)}
.sale-green{left:0;top:18px;width:250px;height:46px;background:var(--green)}
.sale-kid{left:25px;top:0;width:70px;height:82px;background:linear-gradient(#c98a5a,#e2701f)}
.sale-word{left:115px;top:15px;font-family:"Roboto Condensed",sans-serif;font-size:44px;color:#fff}
.vbs{left:274px;top:8px;font-family:"Roboto Condensed",sans-serif;font-size:28px;color:var(--blue)}
.upto{left:274px;top:40px;font-family:"Roboto Condensed",sans-serif;font-size:13px;line-height:13px;color:var(--green)}
.pct{left:303px;top:34px;font-family:"Roboto Condensed",sans-serif;font-size:44px;line-height:44px;color:var(--green)}
.feature{left:0;top:877px;width:695px;height:197px;background:var(--band)}
.feature h3{position:absolute;left:93px;top:44px;font-size:20px;font-weight:600;color:#333}
.feature p{position:absolute;left:93px;top:77px;width:230px;font-size:7.5px;line-height:10px;color:#444}
.feature .cta{position:absolute;left:93px;top:130px;width:97px;height:18px;background:var(--orange);color:#fff;font-size:7.5px;text-align:center;line-height:18px}
.footer{left:0;top:1074px;width:695px;height:99px;background:#fff}
.col{position:absolute;top:16px}
.col h4{font-size:10px;font-weight:600;color:#333;margin-bottom:6px}
.col li{list-style:none;font-size:7px;color:#666;line-height:12.3px}
.news-box{width:120px;height:17px;border:1px solid #ddd;font-size:6.5px;line-height:15px;padding-left:5px;position:relative;color:#555}
.news-go{position:absolute;right:-1px;top:-1px;width:18px;height:17px;background:var(--orange)}
.news-note{font-size:6.5px;color:#666;line-height:9px;margin-top:3px;width:120px}
.bottom{left:0;top:1173px;width:695px;height:27px;background:var(--footer-dark)}
.bottom .copy{left:93px;top:9px;font-size:6px;color:#ddd}
.bottom .mark{left:520px;top:4px;font-size:15px;font-weight:700;color:var(--teal)}
</style>
</head>
<body>
<div class="abs topbar">
  <span class="abs promo">Get your free promo code here</span>
  <span class="abs ship">Free Shipping on All Orders Over $59!</span>
  <span class="abs chat">Live Chat</span>
  <span class="abs acct">Your Account</span>
  <span class="abs cart">Cart</span>
  <span class="abs count">0</span>
</div>

<div class="abs brand">Brightloop</div>
<div class="abs search">Search by Product</div>
<div class="abs search-btn">
  <svg width="30" height="23" viewBox="0 0 30 23"><circle cx="14" cy="10.5" r="4.5" fill="none" stroke="#fff" stroke-width="2"/><line x1="17.2" y1="13.7" x2="20" y2="16.5" stroke="#fff" stroke-width="2"/></svg>
</div>
<div class="abs phone">1-800-555-0147</div>
<div class="abs hours">Open Daily 9am - 8pm EST</div>

<nav class="abs nav">
  <div class="abs nav-inner">
    <span>Party Supplies</span><span>Occasions &amp; Events</span><span>Toys &amp; Games</span><span>Crafts</span><span>Teaching Supplies</span><span>Wedding</span><span>Holidays</span>
  </div>
</nav>

<section class="abs hero-main" role="img" aria-label="Children opening colourful filled party bags outdoors">
  <div class="abs hero-card">
    <div class="script">filled</div>
    <h2>PARTY BAGS</h2>
    <p>Save time &amp; money with our filled party bag kits!</p>
    <span class="shop-btn">SHOP NOW</span>
  </div>
</section>
<section class="abs hero-side" role="img" aria-label="Themed party kit table with plates and cups">
  <div class="abs save-card">
    <div class="script">save</div>
    <p>UP TO 15%<br>ON PARTY KITS</p>
  </div>
  <span class="shop-btn">SHOP NOW</span>
</section>

<div class="abs photo" style="left:93px;top:261px;width:251px;height:220px;background:radial-gradient(circle at 50% 60%,#7a3c8a,#111 70%)" role="img" aria-label="Glow sticks and glowing balls"></div>
<div class="abs label" style="left:93px;top:481px;width:251px;height:27px;line-height:27px">PRODUCT NAME</div>

<div class="abs photo tile-img" style="left:347px;top:261px;width:126px;height:97px;background:linear-gradient(135deg,#fff,#e8dcc4 50%,#b8463c 75%,#fff)" role="img" aria-label="Feathered masquerade masks"></div>
<div class="abs label" style="left:347px;top:358px;width:126px;height:25px;line-height:25px">PRODUCT NAME</div>
<div class="abs photo tile-img" style="left:477px;top:261px;width:125px;height:97px;background:linear-gradient(135deg,#fff 30%,#222 60%,#fff)" role="img" aria-label="Black patterned costume tights"></div>
<div class="abs label" style="left:477px;top:358px;width:125px;height:25px;line-height:25px">PRODUCT NAME</div>

<div class="abs photo" style="left:347px;top:386px;width:126px;height:98px;background:radial-gradient(circle at 50% 60%,#6a8ad8,#0d0d16 70%)" role="img" aria-label="Bundle of glow sticks"></div>
<div class="abs label" style="left:347px;top:484px;width:126px;height:24px;line-height:24px">PRODUCT NAME</div>
<div class="abs photo" style="left:477px;top:386px;width:125px;height:98px;background:radial-gradient(circle,#fff 22%,#254a2a 40%,#2e6b33 55%,#fff 72%)" role="img" aria-label="Green tinsel wreath"></div>
<div class="abs label" style="left:477px;top:484px;width:125px;height:24px;line-height:24px">PRODUCT NAME</div>

<section class="abs sale">
  <div class="abs sale-green"></div>
  <div class="abs sale-kid" role="img" aria-label="Child wearing an orange VBS vest"></div>
  <div class="abs sale-word">SALE</div>
  <div class="abs vbs">VBS FAVORITES</div>
  <div class="abs upto">UP<br>TO</div>
  <div class="abs pct">60% OFF</div>
</section>

<div class="abs photo" style="left:93px;top:615px;width:165px;height:204px;background:linear-gradient(#3f6b3a,#c8302e 60%,#2f5a31)" role="img" aria-label="Santa Claus Christmas tree ornament"></div>
<div class="abs label" style="left:93px;top:819px;width:165px;height:23px;line-height:23px">PRODUCT NAME</div>
<div class="abs photo" style="left:265px;top:619px;width:165px;height:200px;background:linear-gradient(135deg,#f4d21c,#f6b81f 50%,#3a9ad8)" role="img" aria-label="Smiley emoji party tableware"></div>
<div class="abs label" style="left:265px;top:819px;width:165px;height:23px;line-height:23px">PRODUCT NAME</div>
<div class="abs photo" style="left:438px;top:615px;width:164px;height:204px;background:linear-gradient(90deg,#f4f4f4,#3d8c3c 35%,#c23a2e 70%,#f4f4f4)" role="img" aria-label="Two boys playing with colourful slime"></div>
<div class="abs label" style="left:438px;top:819px;width:164px;height:23px;line-height:23px">PRODUCT NAME</div>

<section class="abs feature">
  <h3>O Nazily Posatadak</h3>
  <p>Lorem ipsum dolor sit amet, consectetuer adipiscing elit, sed diam nonummy nibh euismod tincidunt ut laoreet dolore magna aliquam erat volutpat. Ut wisi enim ad minim veniam, quis nostrud exerci tation ullamcorper.</p>
  <span class="cta">Lorem ipsum shop</span>
  <div class="abs" style="left:324px;top:25px;width:284px;height:138px;background:radial-gradient(circle at 27% 50%,transparent 14%,#1f6b2e 16%,#b8352c 28%,transparent 31%),radial-gradient(circle at 73% 50%,transparent 14%,#1b4f5a 16%,#c84ab0 28%,transparent 31%)" role="img" aria-label="Two tinsel holiday wreaths"></div>
</section>

<footer class="abs footer">
  <div class="col" style="left:92px"><h4>Information</h4><ul><li>About Us</li><li>Delivery Information</li><li>Privacy Policy</li><li>Terms &amp; Conditions</li></ul></div>
  <div class="col" style="left:198px"><h4>Customer Service</h4><ul><li>Contact Us</li><li>Returns</li><li>Site Map</li></ul></div>
  <div class="col" style="left:318px"><h4>Extras</h4><ul><li>Brands</li><li>Gift Vouchers</li><li>Affiliates</li><li>Specials</li></ul></div>
  <div class="col" style="left:394px"><h4>My Account</h4><ul><li>My Account</li><li>Order History</li><li>Wish List</li><li>Newsletter</li></ul></div>
  <div class="col" style="left:484px"><h4>Newsletter</h4>
    <div class="news-box">Address Email.<span class="news-go"><svg width="18" height="17" viewBox="0 0 18 17"><polyline points="7,4 11,8.5 7,13" fill="none" stroke="#fff" stroke-width="1.2"/></svg></span></div>
    <p class="news-note">Lorem ipsum dolor sit amet, coseadi piscing elit</p>
  </div>
</footer>

<div class="abs bottom">
  <span class="abs copy">© 2017 Brightloop Shop All Rights Reserved</span>
  <span class="abs mark">Brightloop</span>
</div>
</body>
</html>
```